Disease outbreak warning

I need a flyer that explains to hunters how to act as frontline responders to potential disease outbreaks in wildlife populations. In this case the disease is African Swine Fever. We need an at a glance style with plenty of colour and that’s very easy to read.

I HAVE ATTACHED SOME EXISTING FLYERS FROM OVERSEAS ETC THAT CONTAIN SOME OF THE RELEVANT INFO. THEY ARE TO BE USED AS A GUIDE ONLY.
Updates

Need to see some more options. We have some that can be developed successfully but we’d like to see some more options that will suit a national campaign.

Target Market(s)

Australian hunters encountering wild pigs. Typical age is from 18 to 32 but can be older. Male or female.

Colors

Designer to choose colors to be used in the design.

Requirements
Must have
• The KVRTE logo (supplied). It should be relatively small at the bottom of the page. Plus we need room for two or three other logos that can be overprinted on the project if required.
• Must have information for hunters as the main focus.
Nice to have
• A double sided flyer.
Should not have
• US spelling.

```html
<!DOCTYPE html>
<html lang="en-AU">
<head>
<meta charset="utf-8">
<title>African Swine Fever – Hunters</title>
<link rel="stylesheet" href="https://fonts.googleapis.com/css2?family=Montserrat:ital,wght@0,700;0,800;1,800;1,900&family=Oswald:wght@400&family=Passion+One:wght@400&family=Abril+Fatface&display=swap">
<style>
  :root {
    --red: #e8202a;
    --green: #3fae3a;
    --salmon: #f7a488;
    --orange: #f26b3a;
    --slate: #58595b;
    --grey-bar: #8e8f92;
    --pale: #e4e4e4;
    --ink: #333333;
    --white: #ffffff;
  }
  * { box-sizing: border-box; margin: 0; padding: 0; }
  html, body { width: 848px; height: 1200px; overflow: hidden; background: var(--white); }
  .flyer {
    position: relative; width: 848px; height: 1200px; overflow: hidden;
    background: var(--white); font-family: "Montserrat", Arial, sans-serif;
  }
  .header {
    position: absolute; left: 0; top: 0; width: 848px; height: 170px;
    background: var(--red); color: var(--white); text-align: center;
  }
  .header__title {
    position: absolute; left: 0; right: 0; top: 8px;
    font-weight: 800; font-size: 82px; line-height: 1; letter-spacing: 1px;
  }
  .header__subtitle {
    position: absolute; left: 0; right: 0; top: 92px;
    font-weight: 900; font-style: italic; font-size: 58px; line-height: 1;
  }
  .accent-block { position: absolute; left: 0; top: 178px; width: 185px; height: 250px; background: var(--salmon); }
  .accent-block--dark { left: 120px; top: 178px; width: 65px; height: 60px; background: var(--orange); }
  .side-bar { position: absolute; right: 0; top: 170px; width: 24px; height: 880px; background: var(--grey-bar); }
  .side-bar--low { top: 1075px; height: 125px; background: var(--pale); }

  .info-pill {
    position: absolute; right: 14px; background: var(--green); color: var(--white);
    font-weight: 700; font-size: 18.5px; line-height: 1.35;
    border-radius: 26px 0 0 26px; padding: 14px 20px 14px 24px;
  }
  .info-pill--intro { left: 185px; top: 200px; height: 100px; }
  .info-pill--listing { left: 239px; top: 306px; height: 105px; }

  .portrait {
    position: absolute; left: 26px; top: 292px; width: 142px; height: 142px; border-radius: 50%;
    border: 6px solid var(--orange);
    background: radial-gradient(circle at 50% 45%, #6a5340 0%, #4c3b2c 45%, #6f7d45 100%);
  }

  .hunters-band { position: absolute; left: 0; top: 427px; width: 848px; height: 122px; background: var(--slate); }
  .field-photo {
    position: absolute; left: 0; top: 548px; width: 848px; height: 490px;
    background: radial-gradient(ellipse at 55% 45%, #5a5a5a 0%, #3a3a3a 45%, #8a8a8a 100%);
  }
  .field-photo__stripe { position: absolute; top: 0; height: 490px; width: 20px; background: rgba(255,255,255,0.55); }
  .field-photo__stripe--a { left: 167px; }
  .field-photo__stripe--b { left: 663px; }

  .headline { position: absolute; left: 0; top: 0; width: 848px; height: 1200px; pointer-events: none; }
  .headline__hunters { font-family: "Oswald", Arial, sans-serif; font-size: 250px; fill: var(--white); }
  .headline__warn { font-family: "Passion One", Arial, sans-serif; font-size: 78px; fill: var(--white); }
  .headline__warn .hot { fill: var(--red); stroke: var(--white); stroke-width: 3px; paint-order: stroke; }

  .vaccine-band { position: absolute; left: 0; top: 808px; width: 848px; height: 76px; background: var(--pale); }
  .vaccine-text { font-family: "Abril Fatface", Georgia, serif; font-size: 62px; fill: var(--ink); }
  .vaccine-text .hot { fill: var(--red); }

  .salmon-band { position: absolute; left: 0; top: 1037px; width: 848px; height: 32px; background: var(--salmon); }
  .info-pill--action {
    left: 86px; right: 78px; top: 942px; height: 134px;
    border-radius: 30px; padding: 18px 26px; font-size: 18.5px;
  }

  .partner { position: absolute; bottom: 26px; display: flex; align-items: center; gap: 10px; }
  .partner--client { left: 22px; }
  .partner__dot { width: 44px; height: 44px; border-radius: 50%; background: var(--green); }
  .partner__name { font-weight: 800; font-size: 24px; color: var(--ink); }
  .badge { position: absolute; right: 52px; bottom: 34px; width: 92px; height: 92px; border-radius: 50%; background: var(--red); }
</style>
</head>
<body>
<main class="flyer">
  <header class="header">
    <h1 class="header__title">AFRICAN</h1>
    <p class="header__subtitle">SWINE FEVER</p>
  </header>

  <div class="accent-block"></div>
  <div class="accent-block accent-block--dark"></div>
  <div class="side-bar"></div>
  <div class="side-bar side-bar--low"></div>

  <p class="info-pill info-pill--intro">African swine fever (ASF) is a highly contagious haemorrhagic viral disease of domestic and wild pigs, which is responsible for serious economic and production losses.</p>
  <p class="info-pill info-pill--listing">ASF is a disease listed in the Global Council for Animal Health (GCAH) Terrestrial Animal Health Code and must be reported to the GCAH.</p>

  <div class="portrait" role="img" aria-label="Photo of a wild warthog in grassland"></div>

  <div class="hunters-band"></div>
  <div class="field-photo" role="img" aria-label="Greyscale photo of a wild boar in the bush">
    <div class="field-photo__stripe field-photo__stripe--a"></div>
    <div class="field-photo__stripe field-photo__stripe--b"></div>
  </div>
  <div class="vaccine-band"></div>

  <svg class="headline" viewBox="0 0 848 1200" aria-label="Hunters, don't be the carrier of swine fever. There is no vaccine against it">
    <text class="headline__hunters" x="36" y="648" textLength="776" lengthAdjust="spacingAndGlyphs">HUNTERS</text>
    <text class="headline__warn" x="180" y="700" textLength="584" lengthAdjust="spacingAndGlyphs"><tspan class="hot">Don’t</tspan> be the carrier</text>
    <text class="headline__warn" x="188" y="802" textLength="474" lengthAdjust="spacingAndGlyphs">of <tspan class="hot">swine fever</tspan></text>
    <text class="vaccine-text" x="100" y="874" textLength="650" lengthAdjust="spacingAndGlyphs">There is <tspan class="hot">no vaccine</tspan> against it</text>
  </svg>

  <div class="salmon-band"></div>
  <p class="info-pill info-pill--action">ASF is not a danger to human health but it is devastating for farming economy.<br>As hunters, you have both the opportunity to detect cases early and the responsibility to act appropriately.</p>

  <div class="partner partner--client">
    <span class="partner__dot"></span>
    <span class="partner__name">KVRTE</span>
  </div>
  <div class="badge"></div>
</main>
</body>
</html>
```